Vitamin/Dietary Supplement Company needs a simple Hemp CBD Health retail website to display a few...

We need a simple website designed that will allow us to display a few products for purchase. We are a vitamin/dietary supplement company that wants to set up a separate website for CBD health products. CBD is a chemical compound found in hemp and cannabis plants that provide various health and medicinal benefits. Our target audience are individuals that suffer from health issues and would like to treat their pain relief with CBD as an alternative to prescription medication and over the counter drugs such as Paxorin and Lumex. Looking for a simple and clean website that is easy for customers to navigate and purchase products.

Target Market(s)

Our target audience are individuals that suffer from health issues and would like to treat their pain relief with CBD as an alternative to prescription medication and over the counter drugs such as Paxorin and Lumex.

Coding

Coded - Design and coding required

Font styles to use
Serif

Colors

Designer to choose colors to be used in the design.

Requirements
Nice to have
• Homepage, About page, FAQ page, Contact page, Blog page

```html
<!DOCTYPE html>
<html lang="en">
<head>
<meta charset="utf-8">
<title>Hempwell – CBD Health Products</title>
<link href="https://fonts.googleapis.com/css2?family=Poppins:ital,wght@0,300;0,400;0,500;0,600;0,700;1,400&display=swap" rel="stylesheet">
<style>
:root{
  --green:#6ab43e;
  --green-dark:#4f9a26;
  --green-band:#86c232;
  --lime:#9fd33c;
  --ink:#2b2b2b;
  --text:#555;
  --line:#e3e3e3;
  --footer:#1f1f1f;
  --footer-text:#cfcfcf;
  --white:#fff;
}
*{margin:0;padding:0;box-sizing:border-box}
html,body{width:1200px;height:4720px;overflow:hidden}
body{font-family:"Poppins",sans-serif;color:var(--text);background:var(--white);position:relative}
.abs{position:absolute}

/* header */
.brand{position:absolute;left:143px;top:46px;display:flex;align-items:center;gap:12px;font-size:38px;font-weight:600;color:var(--green);letter-spacing:1px}
.brand .dot{width:20px;height:20px;background:var(--green);border-radius:50%}
.toplinks{position:absolute;right:130px;top:25px;display:flex;gap:18px;font-size:11px;color:#555;text-transform:uppercase}
.toplinks span{display:flex;align-items:center;gap:5px}
.toplinks i{display:inline-block;width:9px;height:9px;border:1.5px solid var(--green);border-radius:2px}
.hotline{position:absolute;left:740px;top:64px;width:136px;font-size:13px;color:#333;line-height:20px;text-align:right}
.hotline b{font-weight:500}
.circle-ico{position:absolute;width:30px;height:30px;border-radius:50%;background:var(--green)}
.cart-label{position:absolute;left:970px;top:71px;font-size:14px;color:#444}

.nav{position:absolute;top:128px;left:0;width:1200px;height:53px;background:var(--green)}
.nav ul{list-style:none;display:flex;position:absolute;left:132px;top:0;height:53px}
.nav li{color:var(--white);font-size:15px;font-weight:500;padding:0 18px;line-height:53px;text-transform:uppercase;letter-spacing:.5px}
.nav li.active{background:#8a9a7f}
.search{position:absolute;left:858px;top:14px;width:204px;height:26px;background:var(--white);border-radius:13px;font-size:10px;color:#aaa;padding:6px 12px}

/* hero */
.hero{position:absolute;top:181px;left:0;width:1200px;height:634px;
  background:
    radial-gradient(ellipse 230px 140px at 1080px 300px,rgba(214,70,48,.55),transparent 70%),
    radial-gradient(ellipse 200px 120px at 900px 330px,rgba(170,190,70,.45),transparent 70%),
    radial-gradient(ellipse 260px 220px at 480px 170px,rgba(225,170,140,.75),transparent 70%),
    radial-gradient(ellipse 380px 260px at 300px 430px,rgba(130,125,120,.8),transparent 72%),
    linear-gradient(100deg,#a89f98 0%,#cfc6bd 30%,#ebe6df 58%,#f2eee8 100%)}
.hero-title{position:absolute;right:144px;top:48px;text-align:right;font-size:52px;line-height:66px;font-weight:700;color:#1e1e1e}
.hero-arrow{position:absolute;top:274px;width:42px;height:42px;border:2px solid var(--white);border-radius:50%}
.hero-arrow svg{position:absolute;left:10px;top:10px}

.h2{position:absolute;left:0;width:1200px;text-align:center;font-size:39px;font-weight:500;color:var(--ink)}

/* products */
.product{position:absolute;width:207px}
.product .pic{width:207px;height:210px;border:1px solid var(--line);background:#f3f3f3}
.product .price{margin-top:22px;text-align:center;color:var(--green);font-size:18px;font-weight:600;font-style:italic}
.product .name{margin-top:8px;text-align:center;font-size:15px;line-height:24px;color:#444}
.btn-cart{display:block;margin:14px auto 0;width:120px;height:28px;border:2px solid #333;border-radius:14px;font-size:11px;font-weight:600;line-height:24px;text-align:center;color:#333}

/* band */
.band{position:absolute;top:1795px;left:0;width:1200px;height:596px;background:linear-gradient(180deg,var(--lime),#6fb82c)}
.feature{position:absolute;width:290px;text-align:center;color:var(--white)}
.feature .pic{width:192px;height:192px;margin:0 auto;border-radius:50%;border:5px solid var(--white)}
.feature h3{margin-top:26px;font-size:18px;font-weight:600;line-height:29px;text-transform:uppercase}
.feature p{margin-top:14px;font-size:14px;line-height:24px}

/* welcome */
.intro{position:absolute;top:2478px;left:160px;width:880px;text-align:center;font-size:15px;line-height:27px;color:#444}
.perk{position:absolute;width:210px;text-align:center}
.perk .ring{width:92px;height:92px;border:3px solid #444;border-radius:50%;margin:0 auto;position:relative}
.perk h4{margin-top:28px;font-size:15px;font-weight:600;color:#333;letter-spacing:.5px}
.perk p{margin-top:8px;font-size:12.5px;line-height:21px;color:#666}

/* testimonials */
.testi{position:absolute;top:2871px;left:0;width:1200px;height:537px;background:linear-gradient(180deg,#8ccb2e,var(--green-band))}
.testi h2{position:absolute;top:62px;width:1200px;text-align:center;color:var(--white);font-size:40px;font-weight:600}
.quote{position:absolute;left:291px;top:166px;width:619px;height:167px;background:var(--white);border-radius:8px;padding:22px 40px 0 54px;font-size:12px;line-height:24px;font-style:italic;color:#555}
.quote .mark{position:absolute;font-size:34px;font-weight:700;color:#333;font-style:normal;line-height:1}
.avatar{position:absolute;left:553px;top:304px;width:92px;height:92px;border-radius:50%;background:var(--white);border:4px solid var(--green)}
.testi .who{position:absolute;top:358px;color:var(--white);font-size:17px}
.chev{position:absolute;top:224px;width:26px;height:26px;border-left:2px solid var(--white);border-bottom:2px solid var(--white)}

/* blog */
.post{position:absolute;width:287px}
.post .pic{width:287px;height:178px;position:relative}
.post .date{position:absolute;left:0;bottom:0;width:50px;height:54px;background:var(--green);color:var(--white);text-align:center;font-size:22px;font-weight:600;line-height:26px;padding-top:6px}
.post .date small{display:block;font-size:10px;line-height:12px;font-weight:500}
.post h5{margin-top:20px;font-size:17px;font-weight:400;color:#444}
.post p{margin-top:8px;font-size:12.5px;line-height:22px;color:#666}

/* newsletter */
.news{position:absolute;top:3930px;left:0;width:1200px;height:300px;background:linear-gradient(100deg,#f8faf4,#eef3e6 70%,#e4ecd8)}
.news h2{position:absolute;left:420px;top:58px;font-size:37px;font-weight:600;color:#222;letter-spacing:1px}
.news p{position:absolute;left:420px;top:126px;font-size:15px;line-height:26px;color:#333}
.news .field{position:absolute;left:420px;top:196px;width:461px;height:42px;border:1px solid #d6d6d6;border-radius:21px;background:var(--white);font-size:12px;color:#888;padding:12px 16px}
.news .sub{position:absolute;left:887px;top:196px;width:122px;height:42px;border-radius:21px;background:var(--green);color:var(--white);font-size:14px;font-weight:600;text-align:center;line-height:42px}

/* footer */
.footer{position:absolute;top:4195px;left:0;width:1200px;height:525px;background:var(--footer);color:var(--footer-text)}
.footer h6{position:absolute;top:138px;font-size:17px;font-weight:600;color:var(--white);text-transform:uppercase}
.flist{position:absolute;top:184px;list-style:none;font-size:13px;line-height:29px;color:var(--footer-text)}
.flist li::before{content:"›";margin-right:12px;color:#aaa}
.contact{position:absolute;left:143px;top:180px;font-size:13px;line-height:22px;width:300px}
.contact .row{position:relative;padding-left:36px;margin-bottom:10px}
.contact svg{position:absolute;left:0;top:3px}
.fbrand{position:absolute;left:857px;top:155px;font-size:36px;font-weight:600;color:#e8e8e8;display:flex;align-items:center;gap:10px}
.fbrand .dot{width:20px;height:20px;border-radius:50%;background:var(--green)}
.cards{position:absolute;left:860px;top:232px;display:flex;gap:5px}
.cards span{width:48px;height:28px;border-radius:3px;background:#d9d9d9}
.social{position:absolute;left:940px;top:286px;display:flex;gap:9px}
.social span{width:32px;height:32px;border:2px solid var(--white);border-radius:50%}
.rule{position:absolute;left:0;top:431px;width:1200px;height:1px;background:#333}
.copy{position:absolute;top:462px;width:1200px;text-align:center;font-size:13px;color:var(--footer-text)}
</style>
</head>
<body>

<div class="brand"><span class="dot"></span>Hempwell</div>
<div class="toplinks"><span><i></i>Register</span><span><i></i>Login</span><span><i></i>My Account</span><span><i></i>Checkout</span></div>
<div class="hotline"><b>HotLine / Order:</b><br>0900 555 014</div>
<div class="circle-ico" style="left:884px;top:66px"><svg class="abs" style="left:8px;top:8px" width="14" height="14" viewBox="0 0 14 14"><path d="M3 1 L5 1 L6 4 L4.5 5.5 Q6 8.5 8.5 9.5 L10 8 L13 9 L13 11 Q12 13 10 13 Q2 11 1 3 Q1 1 3 1 Z" fill="#fff"/></svg></div>
<div class="circle-ico" style="left:932px;top:66px"><svg class="abs" style="left:7px;top:8px" width="16" height="14" viewBox="0 0 16 14"><path d="M1 1 H4 L6 9 H13 L15 3 H5" stroke="#fff" stroke-width="1.6" fill="none"/><circle cx="7" cy="12" r="1.4" fill="#fff"/><circle cx="12" cy="12" r="1.4" fill="#fff"/></svg></div>
<div class="cart-label">Shopping Cart</div>

<nav class="nav">
  <ul><li class="active">Home</li><li>About</li><li>Products</li><li>Order Form</li><li>Blog</li><li>Contact Us</li></ul>
  <div class="search">Search</div>
</nav>

<section class="hero" role="img" aria-label="Smiling woman in a grey sweater taking a vitamin capsule beside a bowl of apples and a glass of water">
  <div class="hero-title">VITAMIN<br>SUPPLEMENT</div>
  <div class="hero-arrow" style="left:64px"><svg width="18" height="18" viewBox="0 0 18 18"><path d="M10 3 L4 9 L10 15 M4 9 H16" stroke="#fff" stroke-width="2" fill="none"/></svg></div>
  <div class="hero-arrow" style="left:1093px"><svg width="18" height="18" viewBox="0 0 18 18"><path d="M8 3 L14 9 L8 15 M14 9 H2" stroke="#fff" stroke-width="2" fill="none"/></svg></div>
  <svg class="abs" style="left:0;top:500px" width="1200" height="134" viewBox="0 0 1200 134">
    <path d="M0 134 L0 100 Q600 -40 1200 70 L1200 134 Z" fill="#6ab43e"/>
    <path d="M0 134 L0 120 Q600 -10 1200 95 L1200 134 Z" fill="#fff"/>
  </svg>
</section>

<h2 class="h2" style="top:795px">CBD Health Products</h2>

<div class="product" style="left:143px;top:918px"><div class="pic" role="img" aria-label="Orange pill bottle with capsules" style="background:radial-gradient(ellipse 60px 80px at 55% 48%,#f0a23a,#f6e3c4 70%,#f4f4f4)"></div><div class="price">$25,080</div><div class="name">Phasellus id nisi non libero placerat ultrices</div><span class="btn-cart">ADD TO CART</span></div>
<div class="product" style="left:377px;top:918px"><div class="pic" role="img" aria-label="White supplement bottle with herbal label and tablets" style="background:radial-gradient(ellipse 55px 80px at 50% 48%,#9cc37a,#e7efe0 65%,#f4f4f4)"></div><div class="price">$25,080</div><div class="name">Phasellus id nisi non libero placerat ultrices</div><span class="btn-cart">ADD TO CART</span></div>
<div class="product" style="left:614px;top:918px"><div class="pic" role="img" aria-label="Orange pill bottle with grey cap" style="background:radial-gradient(ellipse 45px 80px at 50% 50%,#e8802c,#f5dcc0 65%,#f4f4f4)"></div><div class="price">$25,080</div><div class="name">Phasellus id nisi non libero placerat ultrices</div><span class="btn-cart">ADD TO CART</span></div>
<div class="product" style="left:850px;top:918px"><div class="pic" role="img" aria-label="Green herbal capsules" style="background:radial-gradient(ellipse 85px 55px at 55% 45%,#4fa12c,#d5ebc7 65%,#f4f4f4)"></div><div class="price">$25,080</div><div class="name">Phasellus id nisi non libero placerat ultrices</div><span class="btn-cart">ADD TO CART</span></div>

<div class="product" style="left:143px;top:1326px"><div class="pic" role="img" aria-label="Amber capsule bottle with white cap" style="background:radial-gradient(ellipse 50px 70px at 50% 52%,#d9731f,#f3d8bc 65%,#f4f4f4)"></div><div class="price">$25,080</div><div class="name">Phasellus id nisi non libero placerat ultrices</div><span class="btn-cart">ADD TO CART</span></div>
<div class="product" style="left:377px;top:1326px"><div class="pic" role="img" aria-label="Brown glass supplement jar" style="background:radial-gradient(ellipse 45px 80px at 50% 50%,#a9541c,#ecd2bd 65%,#f4f4f4)"></div><div class="price">$25,080</div><div class="name">Phasellus id nisi non libero placerat ultrices</div><span class="btn-cart">ADD TO CART</span></div>
<div class="product" style="left:614px;top:1326px"><div class="pic" role="img" aria-label="Dark bottle with orange softgel capsules" style="background:radial-gradient(ellipse 70px 75px at 50% 55%,#5b2b16,#e8cbb3 65%,#f4f4f4)"></div><div class="price">$25,080</div><div class="name">Phasellus id nisi non libero placerat ultrices</div><span class="btn-cart">ADD TO CART</span></div>
<div class="product" style="left:850px;top:1326px"><div class="pic" role="img" aria-label="Black powder supplement tub" style="background:radial-gradient(ellipse 50px 75px at 50% 50%,#161616,#cfcfcf 65%,#f4f4f4)"></div><div class="price">$25,080</div><div class="name">Phasellus id nisi non libero placerat ultrices</div><span class="btn-cart">ADD TO CART</span></div>

<section class="band">
  <div class="feature" style="left:132px;top:86px"><div class="pic" role="img" aria-label="Spoon of colourful vitamin capsules" style="background:radial-gradient(circle at 45% 55%,#f2c15a,#d8762c 45%,#9b3c22 80%,#6f9a3a)"></div><h3>Vitamin/Dietary<br>Supplement</h3><p>Sed ut perspiciatis unde omnis iste natus error sit voluptatem accusantium doloremque laudantium, totam rem aperiam, eaque ipsa quae</p></div>
  <div class="feature" style="left:454px;top:86px"><div class="pic" role="img" aria-label="Medicine bottles with herbs and a mortar" style="background:radial-gradient(circle at 50% 60%,#8a4a22,#e7e0d4 45%,#c2b7a6 75%,#7f9a6a)"></div><h3>Health and<br>Medicinal Benefits</h3><p>Sed ut perspiciatis unde omnis iste natus error sit voluptatem accusantium doloremque laudantium, totam rem aperiam, eaque ipsa quae</p></div>
  <div class="feature" style="left:776px;top:86px"><div class="pic" role="img" aria-label="Hemp plants growing in a greenhouse" style="background:radial-gradient(circle at 50% 35%,#e6efe0,#8bb26e 40%,#355b2c 75%,#1e2e1c)"></div><h3>Hemp and<br>Cannabis Plants</h3><p>Sed ut perspiciatis unde omnis iste natus error sit voluptatem accusantium doloremque laudantium, totam rem aperiam, eaque ipsa quae</p></div>
  <svg class="abs" style="left:0;top:500px" width="1200" height="96" viewBox="0 0 1200 96">
    <path d="M0 96 L0 60 Q600 -20 1200 50 L1200 96 Z" fill="#d7ec9a"/>
    <path d="M0 96 L0 70 Q600 0 1200 72 L1200 96 Z" fill="#fff"/>
  </svg>
</section>

<h2 class="h2" style="top:2407px;font-size:34px">Welcome To Hempwell</h2>
<p class="intro">Sed ut perspiciatis unde omnis iste natus error sit voluptatem accusantium doloremque laudantium, totam rem aperiam, eaque ipsa quae ab illo inventore veritatis et quasi architecto beatae vitae dicta sunt explicabo. Nemo enim ipsam voluptatem quia voluptas sit aspernatur aut odit aut fugit, sed quia consequuntur magni dolores</p>

<div class="perk" style="left:133px;top:2611px"><div class="ring"><svg class="abs" style="left:26px;top:26px" width="40" height="40" viewBox="0 0 40 40"><path d="M4 18 L18 4 L34 4 L34 20 L20 34 Z" fill="#444"/><circle cx="27" cy="11" r="3" fill="#fff"/></svg></div><h4>GREAT VALUE</h4><p>Sed ut perspiciatis unde omnis iste natus sit voluptatem</p></div>
<div class="perk" style="left:369px;top:2611px"><div class="ring"><svg class="abs" style="left:24px;top:26px" width="40" height="40" viewBox="0 0 40 40"><path d="M5 21 L15 31 L35 9" stroke="#444" stroke-width="7" fill="none"/></svg></div><h4>EASY TO ORDER</h4><p>Sed ut perspiciatis unde omnis iste natus sit voluptatem</p></div>
<div class="perk" style="left:608px;top:2611px"><div class="ring"><svg class="abs" style="left:26px;top:24px" width="40" height="44" viewBox="0 0 40 44"><path d="M20 3 L36 9 L36 22 Q36 36 20 42 Q4 36 4 22 L4 9 Z" fill="#444"/><path d="M20 10 L29 14 L29 22 Q29 31 20 35 Z" fill="#fff"/></svg></div><h4>SAFE PAYMENT</h4><p>Sed ut perspiciatis unde omnis iste natus sit voluptatem</p></div>
<div class="perk" style="left:844px;top:2611px"><div class="ring"><svg class="abs" style="left:27px;top:24px" width="38" height="42" viewBox="0 0 38 42"><path d="M12 14 V10 Q12 4 19 4 Q26 4 26 10 V14" stroke="#444" stroke-width="4" fill="none"/><rect x="4" y="14" width="30" height="24" rx="3" fill="#444"/></svg></div><h4>SHOP WITH CONFIDENCE</h4><p>Sed ut perspiciatis unde omnis iste natus sit voluptatem</p></div>

<section class="testi">
  <h2>What Our Clients Say</h2>
  <div class="chev" style="left:152px;transform:rotate(45deg)"></div>
  <div class="chev" style="left:1025px;transform:rotate(-135deg)"></div>
  <div class="quote">
    <span class="mark" style="left:22px;top:20px">“</span>
    Nemo enim ipsam voluptatem quia voluptas sit aspernatur aut odit aut fugit, sed quia constur magni dolores eos qui ratione voluptatem sequi nesciunt. Neque porro quisquam est, qui do-lorem ipsum quia dolor sit amet, consectetur, adipisci velit, sed quia non numquam eius modi tempora incidunt ut labore et dolore magnam aliquam
    <span class="mark" style="left:388px;top:118px">”</span>
  </div>
  <div class="avatar"><svg class="abs" style="left:18px;top:14px" width="48" height="56" viewBox="0 0 48 56"><circle cx="24" cy="16" r="12" fill="#6ab43e"/><path d="M2 54 Q2 32 24 32 Q46 32 46 54 Z" fill="#6ab43e"/></svg></div>
  <div class="who" style="left:416px">Rafi Karim</div>
  <div class="who" style="left:672px">Hempwell</div>
  <svg class="abs" style="left:0;top:437px" width="1200" height="100" viewBox="0 0 1200 100">
    <path d="M0 100 L0 70 Q600 -20 1200 60 L1200 100 Z" fill="#dbeeb0"/>
    <path d="M0 100 L0 82 Q600 10 1200 80 L1200 100 Z" fill="#fff"/>
  </svg>
</section>

<h2 class="h2" style="top:3422px;font-size:37px;font-weight:300;letter-spacing:1px"><b style="font-weight:700">FROM</b> THE BLOG</h2>
<article class="post" style="left:143px;top:3530px"><div class="pic" role="img" aria-label="Hand holding pills beside leafy greens and a lemon" style="background:radial-gradient(ellipse 90px 70px at 85% 75%,#e8d03a,transparent 70%),radial-gradient(ellipse 120px 90px at 80% 30%,#6f9a3c,transparent 70%),radial-gradient(ellipse 110px 80px at 40% 50%,#d9a98a,transparent 70%),linear-gradient(120deg,#4a3426,#7a5238)"><div class="date">02<small>FEB</small></div></div><h5>Sed ut perspiciatis unde omnis</h5><p>Vestibulum sagittis, nisl nec pellentesque suscipit, arcu nisi maximus neque, vitae finibus erat odio eu lacus. Citur malesuada</p></article>
<article class="post" style="left:455px;top:3530px"><div class="pic" role="img" aria-label="Capsules spilled from a white bottle onto a wooden table" style="background:radial-gradient(ellipse 90px 60px at 75% 25%,#f3f0ea,transparent 70%),radial-gradient(ellipse 110px 70px at 60% 65%,#e6c79a,transparent 70%),linear-gradient(120deg,#6b3f25,#9c6a44 55%,#5a351f)"><div class="date">02<small>FEB</small></div></div><h5>Sed ut perspiciatis unde omnis</h5><p>Vestibulum sagittis, nisl nec pellentesque suscipit, arcu nisi maximus neque, vitae finibus erat odio eu lacus. Citur malesuada</p></article>
<article class="post" style="left:767px;top:3530px"><div class="pic" role="img" aria-label="Scientist in a white coat inspecting hemp plants" style="background:radial-gradient(ellipse 80px 110px at 25% 55%,#f4f4f2,transparent 70%),linear-gradient(100deg,#cfdcc8,#6a9a54 50%,#2f5a2a)"><div class="date">02<small>FEB</small></div></div><h5>Sed ut perspiciatis unde omnis</h5><p>Vestibulum sagittis, nisl nec pellentesque suscipit, arcu nisi maximus neque, vitae finibus erat odio eu lacus. Citur malesuada</p></article>

<section class="news">
  <h2>JOIN OUR NEWSLETTER</h2>
  <p>Subscribe to our mailing list to receive updates<br>and promotional offers.</p>
  <div class="field">Enter your E - mail</div>
  <div class="sub">SUBSCRIBE</div>
</section>

<footer class="footer">
  <svg class="abs" style="left:0;top:-36px" width="1200" height="90" viewBox="0 0 1200 90">
    <path d="M0 36 Q600 110 1200 20 L1200 36 Q600 124 0 50 Z" fill="#6ab43e"/>
    <path d="M0 50 Q600 124 1200 36 L1200 90 L0 90 Z" fill="#1f1f1f"/>
  </svg>
  <h6 style="left:143px">Contact Us</h6>
  <div class="contact">
    <div class="row"><svg width="16" height="18" viewBox="0 0 16 18"><path d="M8 1 Q14 1 14 7 Q14 11 8 17 Q2 11 2 7 Q2 1 8 1 Z" fill="#fff"/><circle cx="8" cy="7" r="2.4" fill="#1f1f1f"/></svg>ADDRESS<br>48 Meadow Lane, Dunmore, England</div>
    <div class="row"><svg width="16" height="16" viewBox="0 0 14 14"><path d="M3 1 L5 1 L6 4 L4.5 5.5 Q6 8.5 8.5 9.5 L10 8 L13 9 L13 11 Q12 13 10 13 Q2 11 1 3 Q1 1 3 1 Z" fill="#fff"/></svg>Phone: (555) 014-2290</div>
    <div class="row"><svg width="16" height="14" viewBox="0 0 16 12"><rect x="0" y="0" width="16" height="12" rx="1" fill="#fff"/><path d="M0 1 L8 7 L16 1" stroke="#1f1f1f" stroke-width="1.4" fill="none"/></svg>E-mail: hello@hempwell.shop</div>
    <div class="row"><svg width="16" height="16" viewBox="0 0 16 16"><circle cx="8" cy="8" r="8" fill="#fff"/><path d="M8 3 V8 L11 10" stroke="#1f1f1f" stroke-width="1.6" fill="none"/></svg>Opening hours:<br>Mon-Thurs: 9.30-17.30<br>Fri: 9.30-18.00</div>
  </div>
  <h6 style="left:465px">Information</h6>
  <ul class="flist" style="left:465px"><li>About Us</li><li>Contact Us</li><li>Customer Service</li><li>Privacy Policy</li><li>Terms &amp; Conditions</li><li>Orders and Returns</li></ul>
  <h6 style="left:672px">My Account</h6>
  <ul class="flist" style="left:672px"><li>Sign In</li><li>View Cart</li><li>Wishlist</li><li>FAQ</li></ul>
  <div class="fbrand"><span class="dot"></span>Hempwell</div>
  <div class="cards"><span></span><span></span><span></span><span></span></div>
  <div class="social"><span></span><span></span><span></span></div>
  <div class="rule"></div>
  <div class="copy">© 2018 Hempwell. All Rights Reserved.</div>
</footer>

</body>
</html>
```